Waterless soap seeking funky new design

We are looking for a talented designer to create a fresh and appealing label design for one of our current products. We do have a current logo that we really like and use in several places. We would like the new label design to work with and incorporate the current logo.
The product is our Grit Bloom wipe-off soap. It is made by hand, in small batches. We would like the label design to reflect the hand made aspect of the product. We are not requiring the label to be illustrated but we do like the hand drawn and hand made tie. and the illustration does appeal to us.
Please see the attached current logo that we do like. you can see it used in the attached current label, that we DONT like. this is what we are seeking, a new label for our Grit Bloom soap.
The soap is made for real messes, grease, grime and busted knuckles. It is made using natural ingredients. this is not a Men Only product, it is definitely geared toward men and would like the label to reflect that.

Target Market(s)

Mechanics, tradesmen, welders, People who get dirty for a living

Colors
0054AA
0677BA
7BADD7
CADEEF
E8F1F8
EE7325
F08F49
F5BC92
FAE3D3
FDF4ED
EB3D1F
EC4F4E
F09395
F8D3D4
FCEDEE

Requirements
Must have
• Keep the current logo. It can play a smaller role in the label, but we do use this logo else were in other promo items, and we don't want it to be completely gone.
Nice to have
• I would like to have something illustrated, I am not sold on this but I like the idea of a hand drawn(or at least in part) label to tie into the 'hand made' aspect
Should not have
• Current Font styles, We are currently selling product but we don't care for our font styles.

```html
<!DOCTYPE html>
<html lang="en">
<head>
<meta charset="utf-8">
<title>Grit Bloom Wipe-Off Soap Label</title>
<link href="https://fonts.googleapis.com/css2?family=Anton&family=Oswald:wght@400;500;600;700&display=swap" rel="stylesheet">
<style>
  :root{
    --label-red:#EB3D1F;
    --label-yellow:#FBB01A;
    --navy:#133F78;
    --white:#FFFFFF;
    --page:#FFFFFF;
  }
  *{box-sizing:border-box;margin:0;padding:0}
  html,body{width:780px;height:1200px;overflow:hidden;background:var(--page)}
  .canvas{position:relative;width:780px;height:1200px}
  .label{
    position:absolute;left:18px;top:300px;width:744px;height:630px;
    background:var(--label-yellow);
    font-family:'Oswald',sans-serif;
  }
  .band-top{position:absolute;left:0;top:0;width:100%;height:77px;background:var(--label-red)}
  .band-bottom{position:absolute;left:0;bottom:0;width:100%;height:78px;background:var(--label-red)}
  .brand-seal{position:absolute;left:0;top:-40px;width:490px;height:300px;overflow:visible}
  .tagline-top{
    position:absolute;left:0;width:484px;top:312px;text-align:center;
    color:var(--navy);font-family:'Anton',sans-serif;font-size:17px;letter-spacing:.2px;
  }
  .product-name{
    position:absolute;left:0;width:484px;text-align:center;
    font-family:'Anton',sans-serif;color:var(--white);
    -webkit-text-stroke:2.5px var(--navy);paint-order:stroke fill;
    text-shadow:2px 2px 0 var(--navy);line-height:1;
  }
  .product-name.line-one{top:335px;font-size:60px;letter-spacing:-.5px}
  .product-name.line-two{top:405px;font-size:62px;letter-spacing:-1px}
  .claim{position:absolute;top:488px;display:flex;align-items:center;gap:6px;color:var(--navy)}
  .claim-text{font-family:'Oswald',sans-serif;font-weight:600;font-size:15px;line-height:1.15}
  .claim.eczema{left:70px}
  .claim.waterless{left:192px}
  .claim.natural{left:334px}
  .net-size{position:absolute;left:155px;top:560px;color:var(--white);font-family:'Anton',sans-serif;font-size:26px}
  .origin-mark{position:absolute;left:250px;top:563px;display:flex;align-items:center;gap:6px}
  .origin-text{color:var(--white);font-family:'Anton',sans-serif;font-size:14px;line-height:1}
  .info{position:absolute;left:455px;width:270px;color:var(--white)}
  .info-heading{font-weight:500;font-size:19px;line-height:1.15}
  .info-heading.intro{top:27px}
  .info-body{top:95px;color:var(--white);font-weight:400;font-size:12.4px;line-height:1.26}
  .info-body h3{font-weight:500;font-size:16px;line-height:1.1;color:var(--white)}
  .info-body p{margin-bottom:4px}
  .info-body .gap{margin-top:6px}
  .maker{position:absolute;left:455px;top:568px;color:var(--white);font-weight:500;font-size:15px;line-height:1.55}
  .batch{position:absolute;left:636px;top:576px;color:var(--white);font-weight:500;font-size:8px;line-height:1.3}
</style>
</head>
<body>
<main class="canvas">
  <section class="label">
    <div class="band-top"></div>
    <div class="band-bottom"></div>

    <svg class="brand-seal" viewBox="0 -40 490 300" aria-label="Copper Crate Soap Co. seal">
      <circle cx="242" cy="95" r="124" fill="#FBB01A" stroke="#EB3D1F" stroke-width="6"/>
      <text x="242" y="90" text-anchor="middle" font-family="Oswald, sans-serif" font-weight="700" font-size="34" fill="#133F78">COPPER CRATE</text>
      <text x="242" y="128" text-anchor="middle" font-family="Oswald, sans-serif" font-weight="700" font-size="28" fill="#133F78">SOAP CO.</text>
      <path id="seal-arc" d="M92,95 A150,150 0 0 0 392,95" fill="none"/>
      <text font-family="Anton, sans-serif" font-size="17" fill="#133F78" font-style="italic">
        <textPath href="#seal-arc" startOffset="50%" text-anchor="middle">RINSE-FREE CLEANSER FOR HANDS THAT WORK</textPath>
      </text>
    </svg>

    <p class="tagline-top">TOUGH ON GRIME. GENTLE ON SKIN</p>
    <h1 class="product-name line-one">GRIT BLOOM</h1>
    <h2 class="product-name line-two">WIPE-OFF SOAP</h2>

    <div class="claim eczema">
      <svg width="40" height="38" viewBox="0 0 40 38" aria-hidden="true">
        <g fill="#133F78">
          <rect x="12" y="14" width="16" height="16" rx="5"/>
          <rect x="12" y="4" width="4" height="14" rx="2"/>
          <rect x="17" y="2" width="4" height="14" rx="2"/>
          <rect x="22" y="4" width="4" height="14" rx="2"/>
          <rect x="26" y="14" width="4" height="10" rx="2" transform="rotate(25 28 19)"/>
          <path d="M3 10h6M6 7v6M33 30h6M36 27v6" stroke="#133F78" stroke-width="2"/>
        </g>
      </svg>
      <span class="claim-text">Eczema<br>Friendly</span>
    </div>

    <div class="claim waterless">
      <svg width="36" height="36" viewBox="0 0 36 36" aria-hidden="true">
        <circle cx="18" cy="18" r="15" fill="none" stroke="#133F78" stroke-width="2.5"/>
        <path d="M18 8c-4 6-7 9-7 13a7 7 0 0 0 14 0c0-4-3-7-7-13z" fill="none" stroke="#133F78" stroke-width="2.2"/>
        <line x1="8" y1="28" x2="28" y2="8" stroke="#133F78" stroke-width="2.5"/>
      </svg>
      <span class="claim-text">No Water?<br>No Problem.</span>
    </div>

    <div class="claim natural">
      <svg width="46" height="46" viewBox="0 0 46 46" aria-hidden="true">
        <circle cx="23" cy="23" r="20" fill="none" stroke="#133F78" stroke-width="2.5"/>
      </svg>
    </div>

    <p class="net-size">12 oz</p>
    <div class="origin-mark">
      <svg width="38" height="24" viewBox="0 0 38 24" aria-hidden="true">
        <rect width="38" height="24" fill="#FFFFFF"/>
        <g fill="#B22234">
          <rect y="0" width="38" height="2"/><rect y="4" width="38" height="2"/>
          <rect y="8" width="38" height="2"/><rect y="12" width="38" height="2"/>
          <rect y="16" width="38" height="2"/><rect y="20" width="38" height="2"/>
        </g>
        <rect width="16" height="12" fill="#3C3B6E"/>
      </svg>
      <span class="origin-text">MADE<br>IN USA</span>
    </div>

    <p class="info info-heading intro">Handmade in small batches,<br>All-Natural, No fillers</p>

    <div class="info info-body">
      <h3>Description:</h3>
      <p>Copper Crate Grit Bloom is tough where it counts. Built for busted knuckles and real dirt. This no-rinse soap is built to cut grease, grime, and grit without burning cracked hands. With bentonite clay, panthenol, vitamin E and D-Limonene, it powers through the mess – then wipes off clean. Made for mechanics, field workers, and hard- working hands. No water needed. Power clean your hands wherever the job takes you. No rinse. No sting. Just clean</p>
      <h3>Directions:</h3>
      <p>Apply to dry skin. Rub gently to lift dirt and oils. Wipe clean with towel or cloth. Rinsing is optional- effective with or with out water</p>
      <p class="gap">For external use only. Patch test recommended. Discontinue if irritation occurs. See full info at coppercratesoap.com</p>
      <h3>Ingredients:</h3>
      <p>Water (Aqua), Glycerin, Cocamidopropyl Betaine, Decyl Glucoside, Lauryl Glucoside, Tremella Fuciformis (Mushroom) Extract, Avena Sativa (Oat) Kernel Flour, Helianthus Annuus (Sunflower) Seed Oil, Cetearyl Alcohol, Emulsifying Wax NF, Bentonite, Panthenol (Provitamin B5), Tocopherol (Vitamin E), D-Limonene*, Citric Acid, Presolve Plus (Propylene Glycol, Diazolidinyl Urea, Iodopropynyl Butylcarbamate). *From natural citrus peel oils</p>
    </div>

    <p class="maker">Made In Ridgeway, MT<br>coppercratesoap.com</p>
    <p class="batch">Lot#<br><br>Best if used within<br>24 Months of opening</p>
  </section>
</main>
</body>
</html>
```